BRAVO Estate Steward

We require a website built for this company. Logo is also on the attached document. Some info on the company:<br/>To create a work class experience for our clients for property maintenance. A personalised service that deliver’s what landlords need...Quality work, on time and managed from start to finish.<br/>We do things different, our clients deal with one contact, a client manager who manages your maintenance task from start to finish. Our service allows our expert trades people to do what they do best and leave the management/organising to us!<br/>I have drafted up the layout of the web ... very brief at this stage however once we have more info we will add links and can collate more information and provide. <br/>We just want to get a layout of what you think the web should look like and can go from there.

```html
<!DOCTYPE html>
<html lang="en">
<head>
<meta charset="utf-8">
<title>BRAVO Estate Steward</title>
<link href="https://fonts.googleapis.com/css2?family=Poppins:wght@400;500;600;700&display=swap" rel="stylesheet">
<style>
:root{
  --yellow:#fdc40f;
  --yellow-deep:#f4b800;
  --black:#0d0d0d;
  --ink:#1a1a1a;
  --muted:#555;
  --white:#fff;
}
*{box-sizing:border-box;margin:0;padding:0}
html,body{width:1200px;height:3037px;overflow:hidden}
body{position:relative;font-family:"Poppins",sans-serif;color:var(--ink);background:var(--white)}
.abs{position:absolute}

/* top bar */
.topbar{left:0;top:0;width:1200px;height:38px;background:var(--black);z-index:3;color:#fff;font-size:11px}
.topbar .item{position:absolute;top:11px;display:flex;align-items:center;gap:10px}

/* hero */
.hero{left:0;top:0;width:1200px;height:720px;overflow:hidden}
.hero-photo{position:absolute;inset:0;background:linear-gradient(180deg,#4a4336 0%,#6b5a43 35%,#5a4a35 60%,#3b3628 100%)}
.hero-photo::after{content:"";position:absolute;inset:0;background:rgba(0,0,0,.28)}
.hero-curve{position:absolute;left:0;top:540px}
.brand-badge{left:141px;top:0;width:190px;height:149px;background:var(--yellow);border-radius:0 0 95px 95px;z-index:4;text-align:center;padding-top:26px}
.brand-name{font-size:44px;font-weight:500;line-height:1;color:var(--ink);letter-spacing:1px}
.brand-sub{font-size:11px;font-weight:600;color:var(--white);margin-top:4px;letter-spacing:.3px}
.nav{left:434px;top:72px;z-index:4;display:flex;gap:0;font-size:13px;color:#fff}
.nav a{color:#fff;text-decoration:none;position:absolute;white-space:nowrap}
.search{left:960px;top:65px;width:31px;height:31px;border-radius:50%;background:#fff;z-index:4;display:flex;align-items:center;justify-content:center}
.hero-title{left:0;width:1200px;top:216px;text-align:center;font-size:50px;font-weight:700;color:#fff;z-index:2}
.hero-text{left:300px;width:600px;top:296px;text-align:center;font-size:12px;line-height:23px;color:#fff;z-index:2}
.btn{left:534px;top:369px;width:133px;height:40px;border-radius:20px;background:var(--yellow);color:var(--ink);font-size:12px;font-weight:500;display:flex;align-items:center;justify-content:center;z-index:2}

/* section headings */
.heading{left:0;width:1200px;text-align:center;font-size:34px;font-weight:700;color:var(--ink)}
.rule{width:46px;height:4px;left:577px}

/* about */
.about-text{left:220px;width:760px;top:707px;text-align:center;font-size:11px;line-height:28px;color:var(--muted)}
.video{left:220px;top:819px;width:760px;height:369px;background:linear-gradient(180deg,#3a3a3c 0%,#3e3630 45%,#2b3336 70%,#30373b 100%)}
.play{left:572px;top:985px;width:57px;height:38px;border-radius:9px;background:#d8392c;display:flex;align-items:center;justify-content:center}

/* services */
.services{left:0;top:1266px;width:1200px;height:774px;background:linear-gradient(135deg,#fdc711 0%,#fbc20a 50%,#f7c41d 100%)}
.card{top:1456px;width:290px;height:427px;background:#fff;border-radius:55px;overflow:hidden;text-align:center}
.card-photo{height:225px;width:100%}
.card h3{font-size:18px;font-weight:700;margin-top:26px}
.card p{font-size:10.5px;line-height:23px;color:var(--muted);padding:0 26px;margin-top:16px}
.arrow{top:1942px;width:38px;height:38px;background:#fff;border-radius:6px;display:flex;align-items:center;justify-content:center}

/* team */
.member{top:2233px;width:290px;text-align:center}
.member-photo{height:248px;width:100%;background:linear-gradient(180deg,#ededed 0%,#e2e0dd 60%,#cdc7c0 100%)}
.member h4{font-size:20px;font-weight:700;margin-top:24px}
.member .role{font-size:12px;color:var(--muted);margin-top:6px}
.socials{display:flex;justify-content:center;margin-top:18px}
.socials span{width:36px;height:34px;border:1px solid #333;margin-left:-1px;display:flex;align-items:center;justify-content:center}
.socials span i{width:12px;height:12px;border-radius:50%;background:#222;display:block}

/* footer */
.footer-curve{left:0;top:2600px}
.footer{left:0;top:2760px;width:1200px;height:277px;background:var(--black);color:#fff}
.foot-brand{left:165px;top:2822px;color:#fff}
.foot-brand .brand-name{color:#fff;font-size:44px}
.foot-brand .brand-sub{color:#fff}
.foot-social{left:170px;top:2896px;display:flex;gap:20px}
.foot-social i{width:34px;height:34px;border-radius:50%;background:#fff;display:block}
.copy{left:154px;top:2976px;font-size:11px;color:#ddd}
.foot-h{font-size:14px;font-weight:600;color:#fff}
.foot-links{left:522px;top:2860px;font-size:12px;line-height:28.3px}
.foot-contact{font-size:11.5px;color:#fff;line-height:21px}
</style>
</head>
<body>

<!-- top bar -->
<div class="abs topbar">
  <div class="item" style="left:676px">
    <svg width="14" height="10" viewBox="0 0 14 10"><rect x=".5" y=".5" width="13" height="9" fill="none" stroke="#fff"/><path d="M.5 .5 7 6l6.5-5.5" fill="none" stroke="#fff"/></svg>
    hello@bravomail.com
  </div>
  <div class="item" style="left:855px">
    <svg width="14" height="14" viewBox="0 0 24 24"><path fill="#fff" d="M6.6 10.8a15 15 0 0 0 6.6 6.6l2.2-2.2c.3-.3.7-.4 1-.2 1.1.4 2.3.6 3.6.6.6 0 1 .4 1 1V20c0 .6-.4 1-1 1A17 17 0 0 1 3 4c0-.6.4-1 1-1h3.5c.6 0 1 .4 1 1 0 1.3.2 2.5.6 3.6.1.3 0 .7-.2 1z"/></svg>
    +00-123-4567
  </div>
</div>

<!-- hero -->
<section class="abs hero">
  <div class="hero-photo" role="img" aria-label="Large two-storey villa with arches and palm trees"></div>
  <svg class="hero-curve" width="1200" height="180" viewBox="0 0 1200 180">
    <path d="M0 126 C300 30 800 0 1200 30 L1200 180 L0 180 Z" fill="var(--yellow)"/>
    <path d="M0 170 C320 70 820 22 1200 45 L1200 180 L0 180 Z" fill="#fff"/>
  </svg>
</section>

<div class="abs brand-badge">
  <div class="brand-name">BRAVO</div>
  <div class="brand-sub">ESTATE STEWARD</div>
</div>

<nav class="abs nav">
  <a style="left:0">Home</a>
  <a style="left:99px">About Us</a>
  <a style="left:215px">Services</a>
  <a style="left:327px">Benefit</a>
  <a style="left:432px">Contact Us</a>
</nav>
<div class="abs search">
  <svg width="12" height="12" viewBox="0 0 12 12"><circle cx="5" cy="5" r="3.8" fill="none" stroke="#222" stroke-width="1.3"/><path d="M8 8l3 3" stroke="#222" stroke-width="1.3"/></svg>
</div>

<h1 class="abs hero-title">BRAVO Estate Steward</h1>
<p class="abs hero-text">Cras in ipsum tincidunt, malesuada sapien vitae, vulputate sem. Fusce ut hendrerit magna. Nunc consequat nisl semper sapien aliquam fermentum</p>
<div class="abs btn">Read More</div>

<!-- about -->
<h2 class="abs heading" style="top:636px">About Us</h2>
<div class="abs rule" style="top:685px;background:var(--yellow)"></div>
<p class="abs about-text">Phasellus nec risus viverra, accumsan est ac, maximus leo. Fusce mollis suscipit turpis, ac blandit erat sodales ac. Duis venenatis, purus sodales condimentum pellentesque, turpis eros sodales arcu, nec vehicula sem ligula et eros. Quisque gravida nisl velit, at faucibus elit ultricies non. Nulla varius tellus in dui auctor consequat. Nullam pulvinar leo volutpat metus vehicula, a posuere</p>
<div class="abs video" role="img" aria-label="Video still of a timber lodge beside a pool at dusk"></div>
<div class="abs play"><svg width="18" height="20" viewBox="0 0 18 20"><path d="M0 0 18 10 0 20Z" fill="#fff"/></svg></div>

<!-- services -->
<section class="abs services" role="img" aria-label="Yellow-tinted backdrop of a workshop scene"></section>
<h2 class="abs heading" style="top:1340px">Our Services</h2>
<div class="abs rule" style="top:1389px;background:#fff"></div>

<div class="abs card" style="left:141px">
  <div class="card-photo" role="img" aria-label="Business people shaking hands in an office" style="background:linear-gradient(135deg,#d9d4cc,#8a7f74)"></div>
  <h3>Trade people</h3>
  <p>Vivamus quis orci luctus, varius nulla sed, mattis massa. Orci varius natoque penatibus et magnis dis parturient montes, nascetur ridiculus mus. Donec vulputate</p>
</div>
<div class="abs card" style="left:455px">
  <div class="card-photo" role="img" aria-label="Truck with trailer on a forest highway" style="background:linear-gradient(180deg,#6f8aa6 0%,#3f5a44 45%,#8c8f90 100%)"></div>
  <h3>Removalist van and trailers</h3>
  <p>Vivamus quis orci luctus, varius nulla sed, mattis massa. Orci varius natoque penatibus et magnis dis parturient montes, nascetur ridiculus mus. Donec vulputate</p>
</div>
<div class="abs card" style="left:769px">
  <div class="card-photo" role="img" aria-label="Businessman offering a handshake" style="background:linear-gradient(135deg,#dfe7ee,#2a2c33)"></div>
  <h3>Connections</h3>
  <p>Vivamus quis orci luctus, varius nulla sed, mattis massa. Orci varius natoque penatibus et magnis dis parturient montes, nascetur ridiculus mus. Donec vulputate</p>
</div>

<div class="abs arrow" style="left:551px"><svg width="10" height="12" viewBox="0 0 10 12"><path d="M7 1 2 6l5 5" fill="none" stroke="#222" stroke-width="1.6"/></svg></div>
<div class="abs arrow" style="left:611px"><svg width="10" height="12" viewBox="0 0 10 12"><path d="M3 1l5 5-5 5" fill="none" stroke="#222" stroke-width="1.6"/></svg></div>

<!-- team -->
<h2 class="abs heading" style="top:2104px">Our Team</h2>
<div class="abs rule" style="top:2153px;background:var(--black)"></div>

<div class="abs member" style="left:141px">
  <div class="member-photo" role="img" aria-label="Portrait of team member"></div>
  <h4>Owen Hale</h4>
  <div class="role">Designation</div>
  <div class="socials"><span><i></i></span><span><i></i></span><span><i></i></span></div>
</div>
<div class="abs member" style="left:455px">
  <div class="member-photo" role="img" aria-label="Portrait of team member"></div>
  <h4>Mara Lindqvist</h4>
  <div class="role">Designation</div>
  <div class="socials"><span><i></i></span><span><i></i></span><span><i></i></span></div>
</div>
<div class="abs member" style="left:769px">
  <div class="member-photo" role="img" aria-label="Portrait of team member"></div>
  <h4>Jude Pryor</h4>
  <div class="role">Designation</div>
  <div class="socials"><span><i></i></span><span><i></i></span><span><i></i></span></div>
</div>

<!-- footer -->
<svg class="abs footer-curve" width="1200" height="162" viewBox="0 0 1200 162">
  <path d="M0 148 C420 150 900 110 1200 10 L1200 162 L0 162 Z" fill="var(--yellow)"/>
  <path d="M0 160 C430 162 920 130 1200 50 L1200 162 L0 162 Z" fill="var(--black)"/>
</svg>
<footer class="abs footer"></footer>

<div class="abs foot-brand">
  <div class="brand-name">BRAVO</div>
  <div class="brand-sub">ESTATE STEWARD</div>
</div>
<div class="abs foot-social"><i></i><i></i><i></i></div>
<div class="abs copy">© 2019 Bravo Estate Steward. All rights reserved.</div>

<div class="abs foot-h" style="left:510px;top:2818px">Quick links</div>
<div class="abs foot-links">Home<br>About Us<br>Services<br>Benefit<br>Contact Us</div>

<div class="abs foot-h" style="left:717px;top:2820px">Contact Details</div>
<svg class="abs" style="left:718px;top:2868px" width="20" height="22" viewBox="0 0 20 22"><path d="M10 1a6 6 0 0 0-6 6c0 5 6 11 6 11s6-6 6-11a6 6 0 0 0-6-6z" fill="none" stroke="#fff"/><circle cx="10" cy="7" r="2.2" fill="none" stroke="#fff"/><ellipse cx="10" cy="19" rx="8" ry="2" fill="none" stroke="#fff"/></svg>
<div class="abs foot-contact" style="left:745px;top:2864px">Phasellus nec risus viverra, accumsan<br>est ac, maximus leo</div>
<svg class="abs" style="left:718px;top:2930px" width="18" height="18" viewBox="0 0 24 24"><path fill="none" stroke="#fff" stroke-width="1.5" d="M6.6 10.8a15 15 0 0 0 6.6 6.6l2.2-2.2c.3-.3.7-.4 1-.2 1.1.4 2.3.6 3.6.6.6 0 1 .4 1 1V20c0 .6-.4 1-1 1A17 17 0 0 1 3 4c0-.6.4-1 1-1h3.5c.6 0 1 .4 1 1 0 1.3.2 2.5.6 3.6.1.3 0 .7-.2 1z"/></svg>
<div class="abs foot-contact" style="left:744px;top:2929px">00-123-4567</div>

</body>
</html>
```